Epoxy Flooring Contractor business card

We need a business card to promote a new addition to our business. We now offer Epoxy Flooring. We would like for the business card to include the images attached. One is our logo, the other is a sample of metallic epoxy flooring, we would like to incorporate that somewhere into the design. I was thinking an icon of a man pushing a concrete grinder and have the color set to the metallic epoxy color. I found a business card sample on this website, I will attach it. It has the icon that we are looking for, or something similar.
Our company name is Brightmore Coatings LLC
Our owners name is Dana Pellow
Phone is 561-847-2916
website is www.brightmore-coatingsllc.com
please let me know if you need any other info

Contact Information for Business Card

Brightmore Coatings LLC
Dana Pellow, owner
Phone: 561-847-2916
Address: P.O Box 8146 Lake Worth, FL 33471
www.Brightmore-CoatingsLLC.com
BrightmoreCoatingsLLC@mailvista.net
Include logo attached
It must include a Clip art of man with concrete grinder
Must include metallic epoxy design attached
Must include the following text
Residential Garage Flooring
Epoxy Countertops
Commercial Epoxy Flooring
Restaurant Flooring
Warehouse Flooring
Licensed & Insured
Free Estimates

Colors

Designer to choose colors to be used in the design.

Requirements
Must have
• Include logo attached
• It must include a Clip art of man with concrete grinder
• Must include metallic epoxy design attached
• Must include the following text
• Garage Epoxy Flooring
• Residential Epoxy Flooring
• Concrete Floor Crack Repairs
• Concrete Floor Grinding
• Commercial & Warehouse Epoxy Flooring
• Restaurant Epoxy Flooring
• Epoxy Countertops
• Non Slip Epoxy Pool Decks
• Textured Finishes, Flakes, Granite Coat, Metallic & Quartz
• FREE ESTIMATES • LICENSED & INSURED

```html
<!DOCTYPE html>
<html lang="en">
<head>
<meta charset="utf-8">
<title>Brightmore Coatings – Business Card</title>
<link href="https://fonts.googleapis.com/css2?family=Open+Sans:wght@400;600&display=swap" rel="stylesheet">
<style>
  :root{
    --stage:#d9dadd;
    --card-white:#ffffff;
    --band:#3f5f87;
    --band-light:#7199cf;
    --name-blue:#8aaee0;
    --ink-blue:#3f5f87;
    --epoxy-deep:#1f3f7a;
    --epoxy-mid:#3d6bb5;
    --epoxy-light:#7fa3d6;
    --epoxy-stone:#5b6470;
    --panel:rgba(70,110,170,.72);
    --white:#ffffff;
  }
  *{box-sizing:border-box;margin:0;padding:0}
  html,body{width:1200px;height:800px;overflow:hidden}
  body{background:var(--stage);font-family:"Open Sans",sans-serif;position:relative}

  .card{position:absolute;left:300px;width:600px;height:343px;overflow:hidden;
        box-shadow:0 6px 16px rgba(0,0,0,.25)}

  .brand{position:absolute;display:flex;align-items:center;gap:14px}
  .brand-name{font-weight:600;letter-spacing:3px;line-height:1.05}
  .brand-dot{border-radius:50%;flex:none}

  /* ---------- back ---------- */
  .card-back{top:40px}
  .epoxy-texture{position:absolute;inset:0;
    background:
      radial-gradient(circle at 15% 80%, var(--epoxy-light) 0, transparent 30%),
      radial-gradient(circle at 85% 70%, var(--epoxy-light) 0, transparent 28%),
      linear-gradient(180deg, var(--epoxy-stone) 0%, var(--epoxy-mid) 35%, var(--epoxy-deep) 100%);}
  .service-panel{position:absolute;left:60px;top:22px;width:480px;height:285px;background:var(--panel);
    color:var(--white);text-align:center}
  .back-brand{left:90px;top:36px}
  .back-brand .brand-name{font-size:28px;color:var(--white)}
  .back-brand .brand-dot{width:44px;height:44px;background:var(--white)}
  .grinder-figure{position:absolute;border-radius:6px}
  .card-back .grinder-figure{right:24px;top:26px;width:70px;height:100px;background:rgba(255,255,255,.8)}
  .service-list{position:absolute;left:0;right:0;top:138px;font-size:13.4px;line-height:19px}

  /* ---------- front ---------- */
  .card-front{top:417px;background:var(--card-white)}
  .front-band{position:absolute;left:0;right:0;bottom:0;height:172px;background:var(--band);
    border-top:6px solid var(--band-light)}
  .band-notch{position:absolute;left:75px;top:165px}
  .front-brand{left:130px;top:46px}
  .front-brand .brand-name{font-size:34px;color:var(--ink-blue)}
  .front-brand .brand-dot{width:56px;height:56px;background:var(--band-light)}
  .card-front .grinder-figure{right:60px;top:40px;width:95px;height:130px;
    background:linear-gradient(180deg,var(--band-light),var(--ink-blue))}
  .owner{position:absolute;left:38px;top:220px;line-height:1.1}
  .owner-name{font-size:21px;color:var(--name-blue);letter-spacing:.5px}
  .owner-title{font-size:14px;color:var(--white)}
  .contact{position:absolute;left:262px;top:200px;color:var(--white);font-size:15px;line-height:22px}
  .contact-line{display:flex;align-items:center;gap:8px}
  .contact svg{width:14px;height:14px;flex:none}
  .contact .indent{padding-left:22px}
</style>
</head>
<body>

<section class="card card-back">
  <div class="epoxy-texture" role="img" aria-label="Blue metallic epoxy floor texture"></div>
  <div class="service-panel">
    <div class="brand back-brand">
      <span class="brand-dot"></span>
      <span class="brand-name">Brightmore<br>Coatings</span>
    </div>
    <div class="grinder-figure" role="img" aria-label="Silhouette of a worker pushing a concrete floor grinder"></div>
    <p class="service-list">
      Garage Epoxy Flooring • Residential Epoxy Flooring<br>
      Concrete Floor Crack Repairs • Concrete Floor Grinding<br>
      Commercial &amp; Warehouse Epoxy Flooring • Epoxy Countertops<br>
      Restaurant Epoxy Flooring • Non Slip Epoxy Pool Decks<br>
      Textured Finishes, Flakes, Granite Coat, Metallic &amp; Quartz<br>
      FREE ESTIMATES • LICENSED &amp; INSURED
    </p>
  </div>
</section>

<section class="card card-front">
  <div class="brand front-brand">
    <span class="brand-dot"></span>
    <span class="brand-name">Brightmore<br>Coatings</span>
  </div>
  <div class="grinder-figure" role="img" aria-label="Silhouette of a worker pushing a concrete floor grinder"></div>
  <div class="front-band"></div>
  <svg class="band-notch" width="36" height="20" viewBox="0 0 36 20"><polygon points="0,0 36,0 18,18" fill="var(--band-light)"/></svg>
  <div class="owner">
    <div class="owner-name">DANA PELLOW</div>
    <div class="owner-title">OWNER</div>
  </div>
  <div class="contact">
    <div class="indent">Brightmore Coatings LLC</div>
    <div class="indent">P.O Box 8146 Lake Worth, FL 33471</div>
    <div class="contact-line">
      <svg viewBox="0 0 24 24"><path fill="var(--white)" d="M6.6 10.8a15 15 0 0 0 6.6 6.6l2.2-2.2c.3-.3.7-.4 1-.2 1.1.4 2.3.6 3.6.6.6 0 1 .4 1 1V20c0 .6-.4 1-1 1A17 17 0 0 1 3 4c0-.6.4-1 1-1h3.5c.6 0 1 .4 1 1 0 1.3.2 2.5.6 3.6.1.3 0 .7-.2 1z"/></svg>
      <span>561-847-2916</span>
    </div>
    <div class="contact-line">
      <svg viewBox="0 0 24 24"><rect x="2" y="5" width="20" height="14" fill="none" stroke="var(--white)" stroke-width="2"/><path d="M2 5l10 8 10-8" fill="none" stroke="var(--white)" stroke-width="2"/></svg>
      <span>BrightmoreCoatingsLLC@mailvista.net</span>
    </div>
    <div class="contact-line">
      <svg viewBox="0 0 24 24" fill="none" stroke="var(--white)" stroke-width="2"><circle cx="12" cy="12" r="10"/><ellipse cx="12" cy="12" rx="4" ry="10"/><path d="M2 12h20"/></svg>
      <span>www.Brightmore-CoatingsLLC.com</span>
    </div>
  </div>
</section>

</body>
</html>
```